Website Design for Keystone Ridge Steelcraft And Decorative Forge LLC

Keystone Ridge Steelcraft & Decorative Forge is a veteran-owned and operated metal fabrication firm with decades of combined experience. We deliver custom, ornamental, and architectural metal solutions designed to meet the demands of commercial construction projects.

Our team specializes in fabricating and installing metal stairs, guardrails, handrails, railings, fencing, and ornamental metals that combined durability, code compliance, and visual appeal. We are a Small Business Enterprise (SBE), Veteran Business Enterprise (VBE), Service-Disabled Veteran-Owned Small Business (SDVOSB), and Veteran Friendly Business Enterprise (VFBE) Certified firm.

We are looking for a designer to create our website so that it can be used at our domain www.keystoneridgesteelcraftllc.example that we have sourced through Hostlark.example

We also have already created our corporate logo through crowdsource that can be incorporated into the web design.

Target Market(s)

General Contractors, Construction Managers, and Architects

Industry/Entity Type

Construction

Coding

Coded - Design and coding required

Number of Pages Required

5+ page

Requirements
Must have
• Company logo (Zip File Uploaded), About Us, Product Solutions, Target Market (See uploaded flyer)
Nice to have
• Patriotic Theme (American)
Should not have
• Web store

```html
<!DOCTYPE html>
<html lang="en">
<head>
<meta charset="utf-8">
<title>Keystone Ridge Steelcraft &amp; Decorative Forge</title>
<link href="https://fonts.googleapis.com/css2?family=Play:wght@400;700&family=Poppins:wght@400;500;600&display=swap" rel="stylesheet">
<style>
:root{
  --navy:#1f4690;
  --navy-deep:#173a7c;
  --red:#c1272d;
  --ink:#111;
  --text:#444;
  --muted:#666;
  --line:#d9dde4;
  --white:#fff;
}
*{margin:0;padding:0;box-sizing:border-box}
html,body{width:1200px;height:4501px;overflow:hidden}
body{font-family:'Poppins',sans-serif;color:var(--text);background:var(--white);position:relative}
.heading{font-family:'Play',sans-serif;font-weight:700}
.btn{position:absolute;background:var(--red);color:#fff;font-size:15px;font-weight:500;display:flex;align-items:center;justify-content:center;text-decoration:none}

/* header */
.site-header{position:absolute;top:0;left:0;width:1200px;height:88px;background:#fff}
.brand{position:absolute;left:62px;top:31px;font-family:'Poppins',sans-serif;font-weight:600;color:var(--navy);font-size:17px;line-height:26px;white-space:nowrap}
.nav{position:absolute;left:340px;top:36px;display:flex;font-size:13px;color:#222}
.nav span{margin-right:38px}
.nav .active{color:var(--navy)}
.site-header .btn{left:967px;top:24px;width:174px;height:41px;font-size:15px}

/* hero */
.hero{position:absolute;top:88px;left:0;width:1200px;height:586px;background:var(--navy);overflow:hidden}
.hero svg{position:absolute;left:0;top:0}
.hero h1{position:absolute;left:61px;top:100px;width:540px;font-size:53px;line-height:61px;color:#fff}
.hero p{position:absolute;left:61px;top:362px;width:540px;font-size:15px;line-height:25px;color:#fff}
.hero .btn{left:61px;top:441px;width:142px;height:38px}

/* markets */
.section-title{position:absolute;left:0;width:1200px;text-align:center;font-size:40px;color:var(--ink)}
.market-card{position:absolute;width:350px;height:375px;overflow:hidden;background:linear-gradient(180deg,#8a939c 0%,#5c6670 45%,#000 78%)}
.market-card .label{position:absolute;left:21px;bottom:28px;right:20px;color:#fff}
.market-card h3{font-family:'Poppins',sans-serif;font-weight:500;font-size:18px;line-height:25px}
.market-card p{font-size:12px;line-height:20px;margin-top:8px}
.market-card .link{display:inline-block;margin-top:8px;font-size:13px;font-style:italic;text-decoration:underline;font-weight:500}

/* about */
.about{position:absolute;top:1660px;left:0;width:1200px;height:602px;background:linear-gradient(120deg,var(--navy-deep),var(--navy) 60%,#2a56a3)}
.about .photo-frame{position:absolute;left:107px;top:76px;width:459px;height:455px;border-right:6px solid var(--red);border-bottom:6px solid var(--red)}
.about .photo{position:absolute;left:0;top:0;width:452px;height:449px;background:linear-gradient(160deg,#9fb8d4,#6c7f93 55%,#c7a35a)}
.about h2{position:absolute;left:632px;top:70px;font-size:38px;color:#fff}
.about .copy{position:absolute;left:632px;top:130px;width:450px;font-size:12.2px;line-height:21px;color:#e8eef8}
.about .copy p{margin-bottom:8px}
.about .btn{left:630px;top:481px;width:143px;height:39px}

/* products */
.subtitle{position:absolute;left:0;width:1200px;text-align:center;font-size:13px;line-height:21px;color:#555}
.product-item{position:absolute;width:273px;height:100px;border-bottom:1px solid var(--line);display:flex;align-items:center}
.product-item.last{border-bottom:none}
.product-item svg{flex:none}
.product-item h4{margin-left:22px;font-family:'Poppins',sans-serif;font-weight:600;font-size:17px;line-height:24px;color:var(--navy)}
.feature{position:absolute;left:376px;top:2463px;width:449px;height:488px;background:linear-gradient(180deg,#4a4440 0%,#2b2724 50%,#000 80%)}
.feature h3{position:absolute;left:29px;top:325px;font-family:'Poppins',sans-serif;font-weight:500;font-size:21px;color:#fff}
.feature p{position:absolute;left:29px;top:362px;width:370px;font-size:12.5px;line-height:20px;color:#eee}
.feature .btn{left:29px;top:420px;width:138px;height:39px}

/* experience */
.experience{position:absolute;top:3026px;left:0;width:1200px;height:548px;background:linear-gradient(100deg,#c9c6c0 0%,#8d8c8a 40%,#44484f 70%,#2b3038)}
.experience h2{position:absolute;left:666px;top:70px;font-size:38px;color:#fff}
.exp-item{position:absolute;left:666px;width:433px;height:61px;display:flex}
.exp-item .ico{width:63px;height:61px;background:var(--navy);display:flex;align-items:center;justify-content:center;flex:none}
.exp-item .txt{flex:1;background:rgba(150,150,150,.55);color:#fff;font-size:13.5px;font-weight:500;line-height:20px;padding:10px 60px 10px 22px}

/* why */
.why-item{position:absolute;width:260px;text-align:center}
.why-item svg{display:block;margin:0 auto}
.why-item h4{margin-top:18px;font-family:'Poppins',sans-serif;font-weight:600;font-size:17px;color:var(--navy)}
.why-item p{margin-top:6px;font-size:12.5px;line-height:20px;color:var(--muted)}

/* footer */
.site-footer{position:absolute;top:4181px;left:0;width:1200px;height:320px;background:var(--navy);color:#fff}
.site-footer .brand-f{position:absolute;left:61px;top:58px;font-family:'Poppins',sans-serif;font-weight:600;font-size:19px}
.site-footer .about-f{position:absolute;left:61px;top:110px;width:360px;font-size:12px;line-height:20px}
.social{position:absolute;left:61px;top:223px;display:flex;gap:12px}
.social span{width:29px;height:29px;background:var(--red);display:block}
.divider{position:absolute;top:55px;width:1px;height:190px;background:rgba(255,255,255,.3)}
.site-footer h5{position:absolute;font-family:'Poppins',sans-serif;font-weight:600;font-size:19px}
.foot-nav{position:absolute;left:548px;top:96px;list-style:none;font-size:12px;line-height:22.5px}
.foot-nav li::before{content:"";display:inline-block;width:7px;height:7px;background:var(--red);border:2px solid #fff;margin-right:14px;vertical-align:middle}
.contact{position:absolute;left:867px;display:flex;align-items:flex-start;font-size:13px;line-height:22px}
.contact .sq{width:29px;height:29px;background:var(--red);display:flex;align-items:center;justify-content:center;margin-right:14px;flex:none}
.copyright{position:absolute;left:0;top:290px;width:1200px;text-align:center;font-size:12px}
</style>
</head>
<body>

<header class="site-header">
  <div class="brand">Keystone Ridge Steelcraft</div>
  <nav class="nav">
    <span class="active">Home</span><span>About Us</span><span>Markets Served</span><span>Product Solutions</span><span>Experience</span><span>Why us</span>
  </nav>
  <a class="btn">Request a Quote</a>
</header>

<section class="hero">
  <svg width="1200" height="586" viewBox="0 0 1200 586">
    <defs>
      <linearGradient id="heroPhoto" x1="0" y1="0" x2="1" y2="1">
        <stop offset="0" stop-color="#c9ccd0"/>
        <stop offset=".5" stop-color="#8e8a86"/>
        <stop offset="1" stop-color="#5d554f"/>
      </linearGradient>
    </defs>
    <polygon points="524,0 1200,0 1200,586 690,586" fill="url(#heroPhoto)" role="img" aria-label="Photo of a woman seated on a steel footbridge stairway"/>
  </svg>
  <h1 class="heading">Veteran-Owned Expertise in Custom &amp; Ornamental Metal Fabrication</h1>
  <p>Delivering precision-built, durable, and code-compliant solutions for commercial construction projects nationwide.</p>
  <a class="btn">Get a Quote</a>
</section>

<section>
  <h2 class="section-title heading" style="top:744px">Markets Served</h2>
  <div class="market-card" style="left:59px;top:821px" role="img" aria-label="Photo of construction workers in hard hats">
    <div class="label"><h3>Commercial<br>Construction Served</h3><p>Lorem Ipsum has been the industry's standard dummy text ever since the 1500s.</p><span class="link">Get a Quote</span></div>
  </div>
  <div class="market-card" style="left:425px;top:821px" role="img" aria-label="Photo of an industrial refinery structure">
    <div class="label"><h3>Industrial<br>Facilities</h3><span class="link">Get a Quote</span></div>
  </div>
  <div class="market-card" style="left:790px;top:821px" role="img" aria-label="Photo of manufacturing plant machinery">
    <div class="label"><h3>Manufacturing<br>Plants</h3><span class="link">Get a Quote</span></div>
  </div>
  <div class="market-card" style="left:243px;top:1212px" role="img" aria-label="Photo of government and defense personnel at a control station">
    <div class="label"><h3>Government &amp;<br>Defense Projects</h3><span class="link">Get a Quote</span></div>
  </div>
  <div class="market-card" style="left:608px;top:1212px;background:linear-gradient(180deg,#6f8a5e 0%,#4a5a44 45%,#000 78%)" role="img" aria-label="Photo of landscaped infrastructure with steps">
    <div class="label"><h3>Built Environment &amp;<br>Infrastructure</h3><span class="link">Get a Quote</span></div>
  </div>
</section>

<section class="about">
  <div class="photo-frame"><div class="photo" role="img" aria-label="Photo of an engineer and a site worker reviewing plans"></div></div>
  <h2 class="heading">About Us</h2>
  <div class="copy">
    <p>Keystone Ridge Steelcraft &amp; Decorative Forge is a veteran-owned and operated metal fabrication firm with decades of combined experience. We deliver custom, ornamental, and architectural metal solutions designed to meet the demands of commercial construction projects.</p>
    <p>Our team specializes in fabricating and installing metal stairs, guardrails, handrails, railings, fencing, and ornamental metals that combine durability, code compliance, and visual appeal. We are a Small Business Enterprise (SBE), Veteran Business Enterprise (VBE), Service-Disabled Veteran-Owned Small Busines (SDVOSB), and Veteran Friendly Business Enterprise (VFBE) Certified firm.</p>
    <p>We bring proven expertise in working with a wide range of metals, including carbon steel, stainless steel, aluminum, copper, and brass. This versatility allows us to provide both functionality and durability along with decorative finishes tailored to our clients' goals.</p>
  </div>
  <a class="btn">Read More</a>
</section>

<section>
  <h2 class="section-title heading" style="top:2332px">Product Solutions</h2>
  <p class="subtitle" style="top:2398px">Fabrication &amp; Installation for Division 5 Metals &amp; Division 32<br>Decorative Fences &amp; Gates.</p>

  <div class="product-item" style="left:59px;top:2474px">
    <svg width="68" height="74" viewBox="0 0 68 74"><polygon points="34,2 65,19 65,55 34,72 3,55 3,19" fill="none" stroke="#1f4690" stroke-width="1.5"/><g stroke="#1f4690" stroke-width="1.8" fill="none"><path d="M22 22v32M46 22v32M22 28h24M22 36h24M22 44h24M22 52h24"/></g></svg>
    <h4>Handrails &amp;<br>Guardrails</h4>
  </div>
  <div class="product-item" style="left:59px;top:2596px">
    <svg width="68" height="74" viewBox="0 0 68 74"><polygon points="34,2 65,19 65,55 34,72 3,55 3,19" fill="none" stroke="#1f4690" stroke-width="1.5"/><g stroke="#1f4690" stroke-width="1.8" fill="none"><rect x="22" y="22" width="24" height="30"/><path d="M28 46l6-8 6 8"/></g></svg>
    <h4>Catwalks &amp;<br>Platforms</h4>
  </div>
  <div class="product-item" style="left:59px;top:2719px">
    <svg width="68" height="74" viewBox="0 0 68 74"><polygon points="34,2 65,19 65,55 34,72 3,55 3,19" fill="#c1272d"/><g stroke="#fff" stroke-width="1.8" fill="none"><path d="M20 28h28M34 28v20M24 48h20M22 22h24v6"/></g></svg>
    <h4>Custom Metal<br>Fabrication</h4>
  </div>
  <div class="product-item last" style="left:59px;top:2841px">
    <svg width="68" height="74" viewBox="0 0 68 74"><polygon points="34,2 65,19 65,55 34,72 3,55 3,19" fill="none" stroke="#1f4690" stroke-width="1.5"/><g stroke="#1f4690" stroke-width="1.8" fill="none"><rect x="20" y="26" width="28" height="22"/><path d="M26 26v22M34 26v22M42 26v22"/></g></svg>
    <h4>Decorative Metal<br>Railings</h4>
  </div>

  <div class="feature" role="img" aria-label="Photo of a fabricator in a hard hat working on metal">
    <h3>Custom Metal Fabrication</h3>
    <p>Lorem Ipsum has been the industry's standard dummy text ever since the 1500s.</p>
    <a class="btn">Read More</a>
  </div>

  <div class="product-item" style="left:866px;top:2474px">
    <svg width="68" height="74" viewBox="0 0 68 74"><polygon points="34,2 65,19 65,55 34,72 3,55 3,19" fill="none" stroke="#1f4690" stroke-width="1.5"/><g stroke="#1f4690" stroke-width="1.8" fill="none"><rect x="19" y="22" width="30" height="30"/><path d="M19 32h30M19 42h30M29 22v30M39 22v30"/></g></svg>
    <h4>Decorative<br>Glazed Railings</h4>
  </div>
  <div class="product-item" style="left:866px;top:2596px">
    <svg width="68" height="74" viewBox="0 0 68 74"><polygon points="34,2 65,19 65,55 34,72 3,55 3,19" fill="none" stroke="#1f4690" stroke-width="1.5"/><g stroke="#1f4690" stroke-width="1.8" fill="none"><path d="M18 52h8v-8h8v-8h8v-8h8"/><path d="M18 44l28-20"/></g></svg>
    <h4>Pan<br>Stairs</h4>
  </div>
  <div class="product-item" style="left:866px;top:2719px">
    <svg width="68" height="74" viewBox="0 0 68 74"><polygon points="34,2 65,19 65,55 34,72 3,55 3,19" fill="none" stroke="#1f4690" stroke-width="1.5"/><g stroke="#1f4690" stroke-width="1.8" fill="none"><path d="M18 32h32M18 42h32M22 28v18M46 28v18M30 32v10M38 32v10"/></g></svg>
    <h4>Pipe &amp; Tube<br>Railings</h4>
  </div>
  <div class="product-item last" style="left:866px;top:2841px">
    <svg width="68" height="74" viewBox="0 0 68 74"><polygon points="34,2 65,19 65,55 34,72 3,55 3,19" fill="none" stroke="#1f4690" stroke-width="1.5"/><g stroke="#1f4690" stroke-width="1.8" fill="none"><rect x="20" y="38" width="14" height="14"/><rect x="34" y="32" width="14" height="20"/><circle cx="30" cy="28" r="5"/></g></svg>
    <h4>Miscellaneous<br>Metals</h4>
  </div>
</section>

<section class="experience" role="img" aria-label="Photo of two professionals walking down outdoor concrete steps">
  <h2 class="heading">Experience Snapshot</h2>
  <div class="exp-item" style="top:150px"><div class="ico"><svg width="34" height="34" viewBox="0 0 34 34" fill="none" stroke="#fff" stroke-width="1.6"><circle cx="9" cy="22" r="6"/><circle cx="25" cy="22" r="6"/><rect x="8" y="6" width="18" height="8"/></svg></div><div class="txt">Decades of combined fabrication experience</div></div>
  <div class="exp-item" style="top:237px"><div class="ico"><svg width="34" height="34" viewBox="0 0 34 34" fill="none" stroke="#fff" stroke-width="1.6"><rect x="8" y="4" width="18" height="26" rx="2"/><path d="M12 12h10M12 18h10M12 24h6"/></svg></div><div class="txt">Proven track record with Fortune 500 manufacturers</div></div>
  <div class="exp-item" style="top:324px"><div class="ico"><svg width="34" height="34" viewBox="0 0 34 34" fill="none" stroke="#fff" stroke-width="1.6"><rect x="5" y="10" width="12" height="20"/><rect x="19" y="4" width="10" height="26"/><path d="M8 16h6M8 22h6M22 10h4M22 16h4"/></svg></div><div class="txt">Government, commercial, and industrial project execution expertise</div></div>
  <div class="exp-item" style="top:411px"><div class="ico"><svg width="34" height="34" viewBox="0 0 34 34" fill="none" stroke="#fff" stroke-width="1.6"><circle cx="17" cy="17" r="13"/><path d="M4 17h26M17 4c-6 7-6 19 0 26M17 4c6 7 6 19 0 26"/></svg></div><div class="txt">On-time, precision-built projects nationwide</div></div>
</section>

<section>
  <h2 class="section-title heading" style="top:3645px">Why Contractors Choose Us</h2>

  <div class="why-item" style="left:59px;top:3738px">
    <svg width="66" height="72" viewBox="0 0 66 72"><polygon points="33,2 63,19 63,53 33,70 3,53 3,19" fill="none" stroke="#9fb0cf" stroke-width="1.5"/><g stroke="#1f4690" stroke-width="1.6" fill="none"><circle cx="28" cy="34" r="10"/><path d="M28 28v6l4 3"/><rect x="36" y="36" width="12" height="10"/></g></svg>
    <h4>Stay On Schedule</h4><p>We deliver projects on time, meeting even aggressive timelines.</p>
  </div>
  <div class="why-item" style="left:333px;top:3738px">
    <svg width="66" height="72" viewBox="0 0 66 72"><polygon points="33,2 63,19 63,53 33,70 3,53 3,19" fill="#c1272d"/><g stroke="#fff" stroke-width="1.6" fill="none"><circle cx="33" cy="30" r="7"/><path d="M28 36l-5 12M38 36l5 12M33 22v-4"/></g></svg>
    <h4>Get the Look You Want</h4><p>From functional handrails to custom ornamental features.</p>
  </div>
  <div class="why-item" style="left:607px;top:3738px">
    <svg width="66" height="72" viewBox="0 0 66 72"><polygon points="33,2 63,19 63,53 33,70 3,53 3,19" fill="none" stroke="#9fb0cf" stroke-width="1.5"/><g stroke="#1f4690" stroke-width="1.6" fill="none"><rect x="22" y="22" width="22" height="16"/><path d="M26 42h14M30 38v4M36 38v4M20 50h26"/></g></svg>
    <h4>Lower Costs Over Time</h4><p>Durable materials reduce maintenance and extend performance</p>
  </div>
  <div class="why-item" style="left:880px;top:3738px">
    <svg width="66" height="72" viewBox="0 0 66 72"><polygon points="33,2 63,19 63,53 33,70 3,53 3,19" fill="none" stroke="#9fb0cf" stroke-width="1.5"/><g stroke="#1f4690" stroke-width="1.6" fill="none"><circle cx="33" cy="30" r="9"/><path d="M27 37l-4 13 6-3 4 5M39 37l4 13-6-3-4 5"/></g></svg>
    <h4>American Made</h4><p>Fabricated with pride in the USA, supporting local industries.</p>
  </div>

  <div class="why-item" style="left:59px;top:3945px">
    <svg width="66" height="72" viewBox="0 0 66 72"><polygon points="33,2 63,19 63,53 33,70 3,53 3,19" fill="none" stroke="#9fb0cf" stroke-width="1.5"/><g stroke="#1f4690" stroke-width="1.6" fill="none"><circle cx="33" cy="35" r="11"/><path d="M33 28v7l5 3"/></g></svg>
    <h4>Stay On Schedule</h4><p>We deliver projects on time, meeting even aggressive timelines.</p>
  </div>
  <div class="why-item" style="left:333px;top:3945px">
    <svg width="66" height="72" viewBox="0 0 66 72"><polygon points="33,2 63,19 63,53 33,70 3,53 3,19" fill="none" stroke="#9fb0cf" stroke-width="1.5"/><g stroke="#1f4690" stroke-width="1.6" fill="none"><circle cx="33" cy="35" r="12"/><circle cx="33" cy="35" r="6"/><path d="M33 23v6M33 41v6M21 35h6M39 35h6"/></g></svg>
    <h4>Get the Look You Want</h4><p>From functional handrails to custom ornamental features.</p>
  </div>
  <div class="why-item" style="left:607px;top:3945px">
    <svg width="66" height="72" viewBox="0 0 66 72"><polygon points="33,2 63,19 63,53 33,70 3,53 3,19" fill="none" stroke="#9fb0cf" stroke-width="1.5"/><g stroke="#1f4690" stroke-width="1.6" fill="none"><path d="M20 34l13-12 13 12M24 32v14h18V32M33 46V36"/></g></svg>
    <h4>Lower Costs Over Time</h4><p>Durable materials reduce maintenance and extend performance</p>
  </div>
  <div class="why-item" style="left:880px;top:3945px">
    <svg width="66" height="72" viewBox="0 0 66 72"><polygon points="33,2 63,19 63,53 33,70 3,53 3,19" fill="none" stroke="#9fb0cf" stroke-width="1.5"/><g stroke="#1f4690" stroke-width="1.6" fill="none"><path d="M20 48h26M24 48V32M42 48V32M33 48V28M20 32l13-8 13 8"/></g></svg>
    <h4>American Made</h4><p>Fabricated with pride in the USA, supporting local industries.</p>
  </div>
</section>

<footer class="site-footer">
  <div class="brand-f">Keystone Ridge Steelcraft</div>
  <p class="about-f">Lorem Ipsum has been the industry's standard dummy text ever since the 1500s, when an unknown printer took a galley of type and scrambled it to make a type specimen book.</p>
  <div class="social" aria-label="Social links"><span></span><span></span><span></span><span></span></div>
  <div class="divider" style="left:510px"></div>
  <div class="divider" style="left:810px"></div>
  <h5 style="left:548px;top:58px">Navigation</h5>
  <ul class="foot-nav">
    <li>Home</li><li>About Us</li><li>Market served</li><li>Product solution</li><li>Experience</li><li>Why us</li><li>Contact</li>
  </ul>
  <h5 style="left:867px;top:56px">Contact Us</h5>
  <div class="contact" style="top:96px"><span class="sq"><svg width="15" height="15" viewBox="0 0 24 24"><path fill="#fff" d="M6.6 10.8a15 15 0 0 0 6.6 6.6l2.2-2.2c.3-.3.7-.4 1-.2 1.1.4 2.3.6 3.6.6.6 0 1 .4 1 1V20c0 .6-.4 1-1 1A17 17 0 0 1 3 4c0-.6.4-1 1-1h3.5c.6 0 1 .4 1 1 0 1.3.2 2.5.6 3.6.1.3 0 .7-.2 1z"/></svg></span><span style="padding-top:3px">+ 555-014-7720</span></div>
  <div class="contact" style="top:142px"><span class="sq"><svg width="15" height="12" viewBox="0 0 24 18"><rect x="1" y="1" width="22" height="16" fill="none" stroke="#fff" stroke-width="2"/><path d="M1 1l11 9 11-9" fill="none" stroke="#fff" stroke-width="2"/></svg></span><span style="width:180px;word-break:break-all">info@keystoneridgesteelcraft.example</span></div>
  <p class="copyright">© Copyright 2025 Harlow &amp; Pike Studio. All rights reserved.</p>
</footer>

</body>
</html>
```